Cobalt Ridge Mini Storage - Ad for half Page

Need half page ad for a publication.
would also like to be able to use in the future
self storage facility - 3 locations, the third opening soon
do not like real busy projects...i have a logo but willing to tweak if needed

```html
<!DOCTYPE html>
<html lang="en">
<head>
<meta charset="utf-8">
<title>Cobalt Ridge Mini Storage – Half Page Ad</title>
<link rel="stylesheet" href="https://fonts.googleapis.com/css2?family=Oswald:wght@500;600&family=Open+Sans:wght@400;600;700;800&display=swap">
<style>
  :root{
    --page:#e9e9e9;
    --white:#ffffff;
    --tan:#c78f58;
    --tan-tile:#dcae7c;
    --brown:#6b3d17;
    --bar:#5a3314;
    --bar-head:#e4bd8d;
    --photo-light:#e4ddd0;
    --photo-mid:#b9ad98;
    --photo-dark:#5d5a55;
  }
  *{box-sizing:border-box;margin:0;padding:0}
  html,body{width:877px;height:1200px;overflow:hidden;background:var(--page)}
  body{font-family:"Open Sans",Arial,sans-serif;position:relative}
  .ad{position:absolute;left:28px;top:364px;width:820px;height:472px;background:var(--white);overflow:hidden;box-shadow:0 6px 14px rgba(0,0,0,.25)}
  .photo{position:absolute;left:348px;top:0;width:472px;height:410px;
    background:radial-gradient(ellipse at 55% 20%,#f2eee6 0%,transparent 45%),
      linear-gradient(90deg,var(--photo-mid) 0%,var(--photo-light) 30%,var(--photo-dark) 52%,var(--photo-light) 72%,var(--photo-mid) 100%)}
  .logo{position:absolute;left:0;top:0;width:348px;height:113px;background:var(--white);display:flex;align-items:center;gap:14px;padding-left:22px}
  .logo-mark{width:46px;height:46px;background:var(--tan)}
  .logo-name{color:var(--brown);font-weight:800;font-size:27px;line-height:1.05}
  .offer{position:absolute;left:0;top:113px;width:348px;height:297px;background:var(--tan);color:var(--white);padding:18px 14px 0;text-align:center}
  .offer h1{font-family:"Oswald",Arial,sans-serif;font-weight:500;font-size:25px;letter-spacing:.2px;line-height:1}
  .perks{font-weight:700;font-size:12.5px;margin-top:9px}
  .units{display:flex;justify-content:space-between;margin-top:16px;padding:0 2px}
  .unit{width:73px}
  .unit-tile{width:71px;height:68px;background:var(--tan-tile);border-radius:6px;display:flex;align-items:center;justify-content:center}
  .unit-label{font-size:7.5px;font-weight:700;line-height:1.25;margin-top:5px}
  .tagline{font-weight:700;font-size:14.5px;line-height:1.35;margin-top:12px}
  .url{display:block;margin:10px auto 0;width:262px;height:20px;border-radius:10px;background:var(--white);color:var(--brown);font-weight:800;font-size:12px;line-height:20px}
  .locations{position:absolute;left:0;top:410px;width:820px;height:62px;background:var(--bar);display:flex;padding:9px 0 0 30px}
  .loc{width:283px;color:var(--white);font-size:10px;line-height:1.45}
  .loc h2{color:var(--bar-head);font-size:11.5px;font-weight:700;text-transform:uppercase;margin-bottom:3px}
  .loc p{display:flex;align-items:center;gap:7px}
  .loc svg{flex:none}
  .soon{color:var(--bar-head);padding-top:9px}
  .soon h2{font-size:11.5px;font-weight:700;text-transform:uppercase}
  .soon p{font-size:10.5px;font-weight:700}
</style>
</head>
<body>
  <div class="ad">
    <div class="photo" role="img" aria-label="Smiling man in a white T-shirt carrying two cardboard boxes along a hallway of roll-up storage unit doors"></div>

    <div class="logo">
      <div class="logo-mark"></div>
      <div class="logo-name">Cobalt Ridge<br>Mini Storage</div>
    </div>

    <div class="offer">
      <h1>SECURE, CONVENIENT SELF-STORAGE</h1>
      <p class="perks">24-Hour Access | Discounts Available | Locked-In Rates</p>
      <div class="units">
        <div class="unit">
          <div class="unit-tile"><svg width="44" height="38" viewBox="0 0 44 38" fill="none" stroke="#fff" stroke-width="3"><path d="M3 14 L22 3 L41 14 V36 H3 Z"/><path d="M10 18 H34 M10 23 H34 M10 28 H34 M10 33 H34" stroke-width="2.5"/></svg></div>
          <p class="unit-label">Climate-Controlled Units</p>
        </div>
        <div class="unit">
          <div class="unit-tile"><svg width="44" height="38" viewBox="0 0 44 38" fill="none" stroke="#fff" stroke-width="3"><path d="M3 14 L22 3 L41 14 V36 H3 Z"/><path d="M10 18 H34 M10 23 H34 M10 28 H34" stroke-width="2.5"/></svg></div>
          <p class="unit-label">Non-Climate-Controlled Units</p>
        </div>
        <div class="unit">
          <div class="unit-tile"><svg width="48" height="38" viewBox="0 0 48 38" fill="none" stroke="#fff" stroke-width="3"><path d="M3 12 L24 3 L45 12 V36 H3 Z"/><rect x="9" y="17" width="26" height="13" rx="2" stroke-width="2.5"/><circle cx="15" cy="31" r="3" fill="#fff"/><circle cx="29" cy="31" r="3" fill="#fff"/></svg></div>
          <p class="unit-label">Boat and RV Storage</p>
        </div>
        <div class="unit">
          <div class="unit-tile"><svg width="46" height="38" viewBox="0 0 46 38" fill="none" stroke="#fff" stroke-width="3"><path d="M3 12 Q23 0 43 12 V36 H3 Z"/><path d="M10 17 H36 V36 M10 17 V36 M10 23 H36 M10 29 H36" stroke-width="2.5"/></svg></div>
          <p class="unit-label">Office and Warehouse Space</p>
        </div>
      </div>
      <p class="tagline">Clean Storage Units for Your Home<br>and Business Property</p>
      <span class="url">www.cobaltridgeministorage.com</span>
    </div>

    <div class="locations">
      <div class="loc">
        <h2>Visit us in San Antonio</h2>
        <p><svg width="9" height="9" viewBox="0 0 10 10" fill="var(--bar-head)"><path d="M2 0 L4 3 L3 4 Q4 6 6 7 L7 6 L10 8 L8 10 Q2 9 0 2 Z"/></svg>(210) 555-0148</p>
        <p><svg width="8" height="10" viewBox="0 0 8 10" fill="var(--bar-head)"><path d="M4 0 A4 4 0 0 1 8 4 Q8 6 4 10 Q0 6 0 4 A4 4 0 0 1 4 0 Z"/></svg>4870 Larkspur Road San Antonio, TX 78263</p>
      </div>
      <div class="loc">
        <h2>Visit us in New Braunfels</h2>
        <p><svg width="9" height="9" viewBox="0 0 10 10" fill="var(--bar-head)"><path d="M2 0 L4 3 L3 4 Q4 6 6 7 L7 6 L10 8 L8 10 Q2 9 0 2 Z"/></svg>(830) 555-0192</p>
        <p><svg width="8" height="10" viewBox="0 0 8 10" fill="var(--bar-head)"><path d="M4 0 A4 4 0 0 1 8 4 Q8 6 4 10 Q0 6 0 4 A4 4 0 0 1 4 0 Z"/></svg>62 Millbrook Ave Suite 110 New Braunfels, TX 78130</p>
      </div>
      <div class="soon">
        <h2>The third&nbsp; locations</h2>
        <p>opening soon</p>
      </div>
    </div>
  </div>
</body>
</html>
```